Coastal Banner Bridge website for creative design and functionality.

Using Wordpress and creative license, create an exciting attractive and super interesting website concept that is easy to navigate, educational, fun, youthful, funny, colourful, global, appealing to all age groups and most businesses who have a use for SIGNS.
Products offered are electronic signs, illuminated channel letters, non-illuminated flat cut and molded letters, specialty products, Wayfinding, large format digital printing, volume printing, programs, rebranding, illuminated cabinet type signs and illuminated freestanding signs.
Services include design (to which ArtHiveHub could be a link), surveys, permits, installations and maintenance.
National refers to CANADA although USA clients who have requirements in Canada or Canadian clients having requirements in the USA are welcome.
Degree of difficulty here is well appreciated. Winner will be selected on basis of creative appeal and uniqueness as well as the designer being able and willing to provide a turnkey service to get the site up and running with or without the help of a lead website designer in Canada.
Domain is coastalbannerbridge.ca primary and coastalbannerbridge.com secondary.
Logo exists. Flow chart concept exists. Intent outline exists.
Site should include galleries, Q & A, ugly or funny signs international encouraging global participation, monitored forum for praise and constructive criticism.
CBB works for the client. Objective is to provide premium quality products of ALL TYPES anywhere, for less than market value, from recognized industry leaders (Links), in a timely manner, with transparency, integrity.
Concept is not new but the difference is degree of honesty, commitment to best value, truthfulness of the statement that 'we work for you'.
Given the challenge of website design, we recognize that a turnkey solution can cost us thousands. In an effort to be consistent with our high client standards, we also intend to be extremely loyal and honest and appreciative of the competition winner over the long term as well as anyone who 'tied' or came close second.
To this end, we feel that $500.00 US is a fair incentive to a competition winner whose 'brainchild' is used in whole or in part with two revisions. To be fair to ourselves, we would not be expected to pay anything if the competition generates nothing that excites us. We will work with ArtHiveHub to define that.
As with our future clients, we will be fair, not greedy and honest in our dealings with vendors including designers who want to work with us moving forward. Your excitement will show in your work. Hopefully, our excitement is evident and contagious.
It is not in our best interest nor Arthivehub's best interest to make the contest entries public information due to what we perceive as being a unique competitive template to virtual sign supply. It is suggested that promotion of the creative material produced by entrants be limited to the home page and not the detailed inner 'beauty' of the concept.
I will provide all competitors with all answers to any questions that come up so that a fair playing field is created.
Thank You,
Tom

Target Market(s)

See general info below

Number of Pages Required

5+ page

Font styles to use
Sans Serif

Requirements
Must have
• Defining your business
• 1. Who is your target market?
• Target market is National, Regional and Local entities who buy signs. Targets are retailers, developers, project managers landlords, marketing personnel, Architects, designers and builder.
• 2. What is the overall purpose of your business?
• To do a better job than the conventional sign shop. Better response, better pricing, better communication, better value.
• 3. What distinguishes you from your competitors?
• CBB does not manufacture. We rely on experienced ‘Links’ to provide quality products, preproduction services like surveys and permits, field services like installation and service.
• 4. Who are your major competitors?
• All sign manufacturers are our competitors. Major competitors are those who do multiple locations or program selling. That said, most sign companies have such accounts. Our Links are also our competitors to some degree although we would respect their relationship under normal conditions.
• 6. What are 3 of your businesses strengths?
• Industry relationships (links), knowledge (25 and 40 years of industry experience respectively), existing contact lists of potential clients
• 7. What are the top 3 business values? We work for the client and pride ourselves on our honesty, transparency and integrity
• 8. Do you have a mission statement? If so please include.
• 9. What is your primary offering?
• Illuminated and non-illuminated channel letters, non-illuminated flat cut and molded and specialty letters, electronic signs, large format digital printing. Freestanding signs, illuminated and non-illuminated cabinet signs (wall signs)
• 10. What is your second offering?
• Design, survey, permits, installation and service and to be treated
• 11. What do your customers want?
• Customers want to be treated fairly. They want to be informed and involved (good communications). They want products on time and on budget and right the first time.
• 12. What is the “Emotional Appeal” you want to establish? The feeling you want to come across. In your text, images and graphics?
• Relaxed, excitement, comfort, calm, humour, seriousness, educational, health , confidence, professionalism, knowledgeable
• Marketing and establishing your brand?
• Brand + Marketing + Consistency = CUSTOMERS
• 1. What are some images that best reflect your company brand? ( list three or more)
• Professional. Knowledgeable, loyal, trustworthy, new, positive, confident, artistic, talented, devoted
• 2. What are some colors that best represent your company?
• Multi-color images with pizzaz. Back for nighttime, white for daytime, red for Canadian
• 3. What is your tagline? If you don’t have a tagline please keep these points in mind when creating a tagline. a. Make it quick and easy to say
• b. Try not to go beyond six words. (little words like “the“, and “and” don’t count)
• c. Something that rolls of your tongue and straight into your customer’s memory.
• d. Make sure it provides information.
• COASTAL BANNER BRIDGE WHERE EXPERIENCE COMES TOGETHER
• Creating your Website
• Please keep in mind that a website can be done in stages. Not everything has to be done before your website goes live. You can add details and blogs, and newsletters as you see fit. Please indicate whether you will need any of these items now or in the future phases of your site.
• 1. Home page think “HOOK” your home page is everything and it’s critical that you instantly hook visitors. Don’t rule out Q&A, the promise of freebies or interesting tips.
• Yes. I want Q & A, ugly and interesting sign gallery from public input, occasional time limited specials for supply of product
• 2. Will you be writing your own content or provide information for us to write it?
• We will work together to create content that we both feel is perfect
• 3. If you are writing your own content will you have someone proof read and edit your content for search engine optimization or will you need us to perform that task?
• You two
• 4. Will you need PayPal on your website?
• No. I have credit card payment capability on our invoices.
• 5. How often will your website need to be updated?
• Weekly hopefully
• 6. Are you thinking of updating your own website?
• Yes
• 7. Will you need a log in account with passwords set up for each customer?
• No
• 8. Will you need a newsletter program for promotions and valuable information? (remember these take time and skill)
• No
• 9. Will you be blogging? (do you have enough information to continue weekly or monthly)
• I don’t think so. I would like to use the Q & A format for that if possible
• 10. How many email accounts will you need to have set up?
• Four should be fine. Two at first
• 11. Will there be any forms on your site and if so how many?
• Quote request form on each product page. Custom order form on Orchid page and maybe the channel letter depot page. We will need a form for submission of photos and artwork (drop box) with file types defined. Design request form with fee schedule
• 12. Will there be a photo gallery and if so how many?
• Yes and several. One for each product. One for for ugly and funny. One for completed CBB projects. Eight to ten.
• 13. Will you need an appointment program for clients to make appointments?
• Yes.
• 14. Do you have a logo?
• Yes
• 15. Do you have an existing website?
• No
• 16. Do you have existing marketing material?
• No BUT each product link (wholesalers) have marketing material and we have permission to use their site content. Eg. Pavo catalog can be downloaded and printed.
• ’
• I do like the static header where viewer has the logo and menu in front of them no matter where they are on the site.
• I don’t like the ‘hamburger’ icon for menu selection – something more personal.
• I like a welcoming atmosphere. Hello. Welcome.
• I would like a glossary of terms page
• Definitely want to encourage ANY questions from ANYBODY that we can respond to with or without research and hence develop and promote FAQ
Nice to have
• See must haves

```html
<!DOCTYPE html>
<html lang="en">
<head>
<meta charset="utf-8">
<title>Coastal Banner Bridge</title>
<link rel="stylesheet" href="https://fonts.googleapis.com/css2?family=Open+Sans:ital,wght@0,400;0,600;0,700;1,400&display=swap">
<style>
:root{
  --red:#c8232c;
  --blue:#0d4f8c;
  --navy:#0b3f73;
  --text:#555b63;
  --muted:#8a8f96;
  --line:#e3e5e8;
  --white:#ffffff;
}
*{box-sizing:border-box;margin:0;padding:0}
html,body{width:1200px;height:2880px;overflow:hidden}
body{font-family:"Open Sans",Arial,sans-serif;color:var(--text);background:var(--white);position:relative}

.site-header{position:absolute;top:0;left:0;width:1200px;height:81px;background:var(--white);display:flex;align-items:center;justify-content:space-between;padding:0 100px;z-index:2}
.brand{display:flex;align-items:center;gap:12px}
.brand-dot{width:40px;height:40px;border-radius:50%;background:var(--navy)}
.brand-name{font-size:27px;font-weight:400;color:var(--red)}
.main-nav{display:flex;gap:46px}
.main-nav a{font-size:12px;font-weight:700;color:#3b3f45;text-decoration:none;letter-spacing:.2px}

.hero{position:absolute;top:81px;left:0;width:1200px;height:492px;
  background:
    linear-gradient(180deg,rgba(0,0,0,0) 55%,rgba(8,10,18,.75) 100%),
    radial-gradient(ellipse 160px 120px at 90px 230px,rgba(255,240,220,.85),rgba(255,200,150,.25) 50%,transparent 100%),
    radial-gradient(ellipse 130px 200px at 540px 200px,rgba(255,210,60,.75),rgba(230,90,30,.35) 55%,transparent 100%),
    radial-gradient(ellipse 170px 150px at 420px 110px,rgba(90,230,200,.55),transparent 100%),
    radial-gradient(ellipse 150px 80px at 520px 330px,rgba(230,40,50,.7),transparent 100%),
    radial-gradient(ellipse 200px 160px at 380px 300px,rgba(255,180,90,.45),transparent 100%),
    radial-gradient(ellipse 260px 340px at 980px 180px,rgba(80,170,255,.6),transparent 100%),
    radial-gradient(ellipse 120px 60px at 760px 440px,rgba(255,190,60,.7),transparent 100%),
    radial-gradient(ellipse 300px 200px at 700px 60px,rgba(60,80,170,.6),transparent 100%),
    linear-gradient(100deg,#2a1c2e 0%,#3c2848 30%,#1c2c52 55%,#15346a 75%,#0a1a36 100%)}
.hero-caption{position:absolute;left:100px;top:345px;width:490px;height:100px;background:rgba(20,22,30,.72);border-left:6px solid var(--red);padding:18px 26px;color:var(--white);font-size:18px;line-height:32px}

.welcome{position:absolute;top:628px;left:0;width:1200px;text-align:center}
.section-title{font-size:23px;font-weight:400;color:var(--blue)}
.section-title strong{font-weight:700}
.welcome p{width:840px;margin:20px auto 0;font-size:11.5px;line-height:25px;color:var(--text)}
.actions{display:flex;justify-content:center;gap:18px;margin-top:20px}
.btn{display:flex;align-items:center;gap:8px;height:40px;padding:0 24px;background:var(--red);color:var(--white);font-size:12px;font-weight:700;border-radius:3px;text-decoration:none}

.services{position:absolute;top:852px;left:0;width:1200px;text-align:center}
.service-grid{display:flex;gap:17px;justify-content:center;margin-top:38px}
.service-card{position:relative;width:238px;height:245px;background:var(--blue);border-radius:3px;color:var(--white);padding-top:32px}
.service-card.is-active{background:var(--red)}
.service-card::after{content:"";position:absolute;left:20px;right:20px;bottom:-24px;height:12px;border-radius:50%;background:radial-gradient(ellipse,rgba(0,0,0,.22),transparent 70%)}
.service-card svg{width:78px;height:78px}
.service-card h3{font-size:19px;font-weight:400;margin-top:20px}
.service-card p{font-size:12px;line-height:21px;margin:8px auto 0;width:196px}

.works{position:absolute;top:1237px;left:0;width:1200px;text-align:center}
.work-grid{display:grid;grid-template-columns:repeat(4,234px);gap:21px 21px;justify-content:center;margin-top:34px}
.work-tile{height:167px}
.t1{background:radial-gradient(ellipse 70px 50px at 40px 140px,rgba(255,200,40,.9),transparent),radial-gradient(ellipse 80px 70px at 170px 50px,rgba(240,60,120,.7),transparent),radial-gradient(ellipse 90px 60px at 60px 50px,rgba(80,140,255,.6),transparent),linear-gradient(135deg,#141a30,#2a1a3a)}
.t2{background:radial-gradient(ellipse 90px 45px at 50% 40%,#ffd060,#e08a20 55%,transparent 100%),radial-gradient(ellipse 70px 50px at 50% 80%,rgba(255,230,160,.8),transparent),linear-gradient(180deg,#1a0a06,#3a1a0a)}
.t3{background:radial-gradient(ellipse 120px 90px at 60% 40%,rgba(80,160,240,.7),transparent),radial-gradient(ellipse 60px 40px at 80% 20%,rgba(240,200,120,.6),transparent),linear-gradient(135deg,#050a14,#16305a,#050a14)}
.t4{background:radial-gradient(ellipse 100px 70px at 50% 50%,rgba(230,240,255,.8),transparent),linear-gradient(135deg,#9cc0e8,#3a6aa8 50%,#1e3e70)}
.t5{background:radial-gradient(ellipse 70px 80px at 150px 70px,rgba(120,240,230,.7),transparent),radial-gradient(ellipse 50px 40px at 40px 130px,rgba(230,70,60,.6),transparent),linear-gradient(135deg,#0e2024,#1c4a50,#0a1416)}
.t6{background:radial-gradient(ellipse 30px 60px at 55% 55%,#ffffff,rgba(255,255,255,.3) 70%,transparent),linear-gradient(180deg,#2a2e34 0%,#8a9098 45%,#c8ccd2 100%)}
.t7{background:radial-gradient(ellipse 60px 40px at 40px 30px,rgba(220,30,40,.95),transparent),radial-gradient(ellipse 60px 40px at 190px 50px,rgba(40,90,220,.9),transparent),radial-gradient(ellipse 80px 40px at 120px 130px,rgba(250,240,230,.85),transparent),linear-gradient(135deg,#1a1420,#2a2a40)}
.t8{background:radial-gradient(ellipse 110px 40px at 55% 55%,rgba(15,20,30,.9),transparent),linear-gradient(180deg,#c8ced6,#7a828c 60%,#4a5058)}

.video-band{position:absolute;top:1755px;left:0;width:1200px;height:440px;
  background:
    linear-gradient(180deg,rgba(0,0,0,0) 60%,rgba(255,220,200,.25) 100%),
    radial-gradient(ellipse 140px 200px at 120px 150px,rgba(240,60,100,.75),transparent 100%),
    radial-gradient(ellipse 90px 160px at 280px 180px,rgba(255,210,60,.6),transparent 100%),
    radial-gradient(ellipse 200px 220px at 1000px 170px,rgba(255,110,40,.7),transparent 100%),
    radial-gradient(ellipse 120px 140px at 820px 90px,rgba(220,40,60,.6),transparent 100%),
    radial-gradient(ellipse 420px 60px at 50% 380px,rgba(255,190,150,.55),transparent 100%),
    radial-gradient(ellipse 80px 140px at 560px 120px,rgba(255,80,90,.5),transparent 100%),
    linear-gradient(180deg,#1c1228 0%,#3a1c34 45%,#6a3042 75%,#8a5a68 100%)}
.play-button{position:absolute;left:558px;top:178px;width:84px;height:84px;border-radius:50%;background:var(--white);display:flex;align-items:center;justify-content:center}

.testimonials{position:absolute;top:2252px;left:0;width:1200px;text-align:center}
.quote-row{display:flex;justify-content:center;gap:40px;margin-top:50px}
.quote{width:312px;text-align:left;position:relative}
.quote blockquote{font-size:11.5px;font-style:italic;line-height:23px;color:var(--text);padding:0 34px 0 26px}
.quote .mark{position:absolute;font-size:34px;color:#b8bcc2;font-style:normal;line-height:1}
.quote .mark.open{left:0;top:-8px}
.quote .mark.close{right:0;top:64px}
.author{display:flex;align-items:center;gap:14px;margin-top:34px;padding-left:6px}
.avatar{width:58px;height:58px;border-radius:50%;border:3px solid var(--blue);background:#d8dde3}
.author-name{font-size:13px;font-weight:700;color:var(--red)}
.author-role{font-size:11.5px;color:var(--muted);margin-top:2px}

.footer-rule{position:absolute;left:16px;right:16px;top:2565px;border-top:1px solid var(--line)}
.site-footer{position:absolute;top:2608px;left:0;width:1200px;height:180px}
.foot-col{position:absolute;top:0}
.foot-col h4{font-size:16px;font-weight:700;color:#2d3138}
.foot-col h4::after{content:"";display:block;width:24px;height:2px;background:var(--blue);margin-top:10px}
.foot-col ul{list-style:none;margin-top:16px}
.foot-col li{font-size:11.5px;line-height:26px;color:var(--text)}
.contact-line{display:flex;align-items:center;gap:8px;font-size:11.5px;line-height:26px}
.socials{display:flex;gap:8px;margin-top:10px}
.socials span{width:30px;height:30px;border-radius:50%}
.s1{background:#2a5aa8}.s2{background:#1a7aa8}.s3{background:#e89a20}.s4{background:#4ab0e0}.s5{background:#d8242a}
.foot-brand{display:flex;align-items:center;gap:10px;margin-top:22px}
.foot-brand .brand-dot{width:38px;height:38px}
.foot-brand .brand-name{font-size:23px}
.bottom-rule{position:absolute;left:16px;right:16px;top:2818px;border-top:1px solid var(--line)}
.copyright{position:absolute;top:2838px;left:0;width:1200px;text-align:center;font-size:11px;color:var(--text)}
</style>
</head>
<body>

<header class="site-header">
  <div class="brand"><span class="brand-dot"></span><span class="brand-name">Coastal Banner Bridge</span></div>
  <nav class="main-nav">
    <a>HOME</a><a>ABOUT US</a><a>SERVICES</a><a>TESTIMONIALS</a><a>WORKS</a><a>CONTACT US</a>
  </nav>
</header>

<section class="hero" role="img" aria-label="Night city street lined with bright illuminated billboards and signs">
  <div class="hero-caption">Our services include surveys, permits, installations and maintenance in Canada.</div>
</section>

<section class="welcome">
  <h2 class="section-title">Welcome to <strong>Coastal Banner Bridge</strong></h2>
  <p>Products we offer are electronic signs, illuminated channel letters, non-illuminated flat cut and molded letters, specialty products, Wayfinding, large format digital printing, volume printing, programs, rebranding, illuminated cabinet type signs and illuminated freestanding signs.</p>
  <div class="actions">
    <a class="btn"><svg width="12" height="14" viewBox="0 0 12 14"><circle cx="7" cy="2" r="1.6" fill="#fff"/><path d="M5 5h3l-2 8H3z" fill="#fff"/></svg>READ MORE</a>
    <a class="btn"><svg width="13" height="13" viewBox="0 0 24 24"><path d="M6.6 10.8a15 15 0 0 0 6.6 6.6l2.2-2.2a1 1 0 0 1 1-.25 11.4 11.4 0 0 0 3.6.6 1 1 0 0 1 1 1V20a1 1 0 0 1-1 1A17 17 0 0 1 3 4a1 1 0 0 1 1-1h3.5a1 1 0 0 1 1 1c0 1.25.2 2.45.6 3.6a1 1 0 0 1-.25 1z" fill="#fff"/></svg>CONTACT US</a>
  </div>
</section>

<section class="services">
  <h2 class="section-title">Services <strong>we provide</strong> are</h2>
  <div class="service-grid">
    <article class="service-card is-active">
      <svg viewBox="0 0 80 80" fill="none" stroke="#fff" stroke-width="2.5"><circle cx="22" cy="22" r="11"/><circle cx="46" cy="22" r="11"/><rect x="12" y="36" width="44" height="28" rx="3"/><path d="M56 44l14-7v26l-14-7z"/></svg>
      <h3>Surveys</h3><p>Lorem Ipsum is simply dummy text of the printing</p>
    </article>
    <article class="service-card">
      <svg viewBox="0 0 80 80" fill="none" stroke="#fff" stroke-width="2.5"><rect x="20" y="8" width="40" height="62" rx="3"/><circle cx="40" cy="34" r="12"/><path d="M28 34h24M40 22c-6 6-6 18 0 24M40 22c6 6 6 18 0 24"/><path d="M30 58h20"/></svg>
      <h3>Permits</h3><p>Lorem Ipsum is simply dummy text of the printing</p>
    </article>
    <article class="service-card">
      <svg viewBox="0 0 80 80" fill="none" stroke="#fff" stroke-width="2.5"><circle cx="40" cy="40" r="10"/><path d="M36 10h8l2 8 6 3 7-4 6 6-4 7 3 6 8 2v8l-8 2-3 6 4 7-6 6-7-4-6 3-2 8h-8l-2-8-6-3-7 4-6-6 4-7-3-6-8-2v-8l8-2 3-6-4-7 6-6 7 4 6-3z"/></svg>
      <h3>Installations</h3><p>Lorem Ipsum is simply dummy text of the printing</p>
    </article>
    <article class="service-card">
      <svg viewBox="0 0 80 80" fill="none" stroke="#fff" stroke-width="2.5"><circle cx="34" cy="28" r="13"/><path d="M10 66c0-14 10-22 24-22s24 8 24 22z"/><path d="M46 16a12 12 0 0 1 2 24M58 46c8 3 13 10 13 20h-10"/></svg>
      <h3>Maintenance</h3><p>Lorem Ipsum is simply dummy text of the printing</p>
    </article>
  </div>
</section>

<section class="works">
  <h2 class="section-title">Our <strong>Works</strong></h2>
  <div class="work-grid">
    <div class="work-tile t1" role="img" aria-label="Busy night street with taxis and lit billboards"></div>
    <div class="work-tile t2" role="img" aria-label="Marquee sign with bulb lights"></div>
    <div class="work-tile t3" role="img" aria-label="Wall of glowing digital screens"></div>
    <div class="work-tile t4" role="img" aria-label="Overhead view of highway interchange"></div>
    <div class="work-tile t5" role="img" aria-label="Illuminated word display panel"></div>
    <div class="work-tile t6" role="img" aria-label="Blank lightbox stand in a concourse"></div>
    <div class="work-tile t7" role="img" aria-label="Cluster of bright advertising displays"></div>
    <div class="work-tile t8" role="img" aria-label="Overhead wayfinding sign in a station"></div>
  </div>
</section>

<section class="video-band" role="img" aria-label="Blurred night traffic through a square full of neon billboards">
  <div class="play-button"><svg width="30" height="32" viewBox="0 0 30 32"><path d="M6 3l22 13L6 29z" fill="#555b63"/></svg></div>
</section>

<section class="testimonials">
  <h2 class="section-title">What our <strong>Client's say</strong></h2>
  <div class="quote-row">
    <figure class="quote">
      <span class="mark open">“</span><span class="mark close">”</span>
      <blockquote>Lorem Ipsum is simply dummy text of the printing and typesetting industry. Lorem Ipsum has been the industry's standard dummy text ever since the 1500s unknown...</blockquote>
      <figcaption class="author"><span class="avatar" role="img" aria-label="Client portrait"></span><span><div class="author-name">MARCUS HALE</div><div class="author-role">Business man</div></span></figcaption>
    </figure>
    <figure class="quote">
      <span class="mark open">“</span><span class="mark close">”</span>
      <blockquote>Lorem Ipsum is simply dummy text of the printing and typesetting industry. Lorem Ipsum has been the industry's standard dummy text ever since the 1500s unknown...</blockquote>
      <figcaption class="author"><span class="avatar" role="img" aria-label="Client portrait"></span><span><div class="author-name">MARCUS HALE</div><div class="author-role">Business man</div></span></figcaption>
    </figure>
    <figure class="quote">
      <span class="mark open">“</span><span class="mark close">”</span>
      <blockquote>Lorem Ipsum is simply dummy text of the printing and typesetting industry. Lorem Ipsum has been the industry's standard dummy text ever since the 1500s unknown...</blockquote>
      <figcaption class="author"><span class="avatar" role="img" aria-label="Client portrait"></span><span><div class="author-name">MARCUS HALE</div><div class="author-role">Business man</div></span></figcaption>
    </figure>
  </div>
</section>

<div class="footer-rule"></div>

<footer class="site-footer">
  <div class="foot-col" style="left:127px">
    <h4>Welcome</h4>
    <ul><li>Home</li><li>About us</li><li>Services</li><li>Testimonials</li><li>Works</li></ul>
  </div>
  <div class="foot-col" style="left:333px">
    <h4>Information</h4>
    <ul><li>Terms &amp; Conditions</li><li>Privacy Policy</li><li>Disclaimer</li><li>Contact us</li><li>Sitemap</li></ul>
  </div>
  <div class="foot-col" style="left:549px">
    <h4>Contact Info</h4>
    <ul>
      <li style="line-height:22px;margin-top:2px">42 Harbour Lane, Port Ellis,<br>Canada : 4471220</li>
      <li class="contact-line"><svg width="11" height="11" viewBox="0 0 24 24"><path d="M6.6 10.8a15 15 0 0 0 6.6 6.6l2.2-2.2a1 1 0 0 1 1-.25 11.4 11.4 0 0 0 3.6.6 1 1 0 0 1 1 1V20a1 1 0 0 1-1 1A17 17 0 0 1 3 4a1 1 0 0 1 1-1h3.5a1 1 0 0 1 1 1c0 1.250.2 2.45.6 3.6a1 1 0 0 1-.25 1z" fill="#c8232c"/></svg>( 555 ) 010 - 2284</li>
      <li class="contact-line"><svg width="12" height="10" viewBox="0 0 24 18"><rect x="1" y="1" width="22" height="16" rx="1" fill="none" stroke="#c8232c" stroke-width="2"/><path d="M1 2l11 8 11-8" fill="none" stroke="#c8232c" stroke-width="2"/></svg>info@coastalbannerbridge.com</li>
    </ul>
  </div>
  <div class="foot-col" style="left:849px">
    <h4>Follow Us</h4>
    <ul><li>Connect with our social network</li></ul>
    <div class="socials"><span class="s1"></span><span class="s2"></span><span class="s3"></span><span class="s4"></span><span class="s5"></span></div>
    <div class="foot-brand"><span class="brand-dot"></span><span class="brand-name">Coastal Banner Bridge</span></div>
  </div>
</footer>

<div class="bottom-rule"></div>
<p class="copyright">© 2017. Coastal Banner Bridge. All rights reserved.</p>

</body>
</html>
```